Guaranteed Job - Sleek Sexy Business Card UV Spot

Im looking for a sleek and sexy business card, that resembles elite or VIP status status.
our business is corinvale.example
you can view our products on there, but our main audience for handing out our cards will be for people in the hospitality industry, so it will need to impress high management and CEO of hotels and restaurants, bars, clubs etc...
the card features will have UV spot on both sides, 400gsm stock. standard size.
Artwork should be 86 x 54mm + 2mm bleed = 90 x 58mm
it should have a nice "unique" uv spot pattern that highlights the card, not a repeated pattern, theres no originality there, and it will be disregarded.
The written material will be:
Corin Vale Hospitality College (logo)
Tobin Marsh
Director
Phone: 1300 615 737
Mobile: 0455 817 296
Email: info@corinvale.example
website: www.corinvale.example
I'm looking for originality here, i don't want just a simple stock card, want something that has a wow factor for people.
You will find the logo attached. you may invert the white to black words to suit the background as you please.
thank you and good luck
As a side note, ive received a lot of proposals, im too busy to give feedback to each and every one, so if i havent provided feedback for your design within 24 hours, then consider it not acceptable, and you could resubmit another design.
So far i have not seen any design that stood out for me, they all seem pretty generic. there nothing thats unique, i would figure for the amount that im offering, that people would put some more effort and creativity into the design.
so far over 200 designs submitted, and nothing i have seen looks very original, everything looks like a different variation of the same stuff, i said it very clearly i wanted something unique, the only thing that has come close to it so far is this one
Reason: Ive received alot of design concepts and i have reviewed everyone, but i havent had time to give feedback to every single one, only the ones that have interested me, if i havent responded, its because i havent found it good enough.
so far only a few design have been on par with what ive been looking for, an attractive eye popping design.
heres a few of them,
http://files.pixelbazaar.example/design_img/51736/62418/62418_2840915_51736_image.jpg
http://files.pixelbazaar.example/design_img/51736/68254/68254_2841377_51736_image.jpg
theyre, both unique and original, and eye catching, the only thing theyre missing is the sexyness.
if you still think you have some creativity left in your minds, then throw it on here.
Reason: Sorry guys for the delay, I was in a serious accident and out of commission for the past few months, I'm just slowly recovering now, please bare with me as i try to attend to this project, it may take me awhile as I have other projects that are on standby, I'm not 100% at the moment, so im extending the deadline for 2 weeks right now. Thanks for your patience.
Hospitality

```html
<!DOCTYPE html>
<html lang="en">
<head>
<meta charset="utf-8">
<title>Corin Vale Hospitality College – Business Card</title>
<link rel="stylesheet" href="https://fonts.googleapis.com/css2?family=Arimo&family=Barlow+Semi+Condensed:wght@500&display=swap">
<style>
  :root {
    --card-black: #000000;
    --ink-white: #ffffff;
    --accent-blue: #7aa6d8;
    --photo-deep: #0a0a14;
    --photo-mid: #1b1c2e;
    --photo-olive: #8fc32a;
    --photo-glass: #3c4256;
  }
  html, body {
    margin: 0;
    padding: 0;
    width: 1200px;
    height: 773px;
    overflow: hidden;
    background: var(--card-black);
  }
  .card {
    position: relative;
    width: 1200px;
    height: 773px;
    background: var(--card-black);
    overflow: hidden;
    font-family: "Arimo", Arial, sans-serif;
    color: var(--ink-white);
  }
  .cocktail-photo {
    position: absolute;
    top: 0;
    right: 0;
    width: 530px;
    height: 773px;
    background:
      radial-gradient(ellipse 260px 140px at 420px 520px, var(--photo-olive) 0%, rgba(143,195,42,0.35) 45%, transparent 75%),
      radial-gradient(ellipse 380px 260px at 360px 450px, var(--photo-glass) 0%, transparent 70%),
      radial-gradient(ellipse 300px 300px at 330px 120px, var(--photo-mid) 0%, transparent 75%),
      linear-gradient(90deg, var(--card-black) 0%, var(--photo-deep) 30%, var(--photo-deep) 100%);
  }
  .brand {
    position: absolute;
    left: 80px;
    top: 80px;
    display: flex;
    align-items: center;
    gap: 34px;
  }
  .brand-square {
    width: 170px;
    height: 170px;
    background: var(--accent-blue);
  }
  .brand-name {
    font-family: "Barlow Semi Condensed", "Arial Narrow", sans-serif;
    font-weight: 500;
    color: var(--ink-white);
    text-transform: uppercase;
    line-height: 1;
    margin: 0;
  }
  .brand-name .line-main {
    display: block;
    font-size: 76px;
    letter-spacing: 1px;
  }
  .brand-name .line-sub {
    display: block;
    font-size: 28px;
    letter-spacing: 1px;
    margin-top: 10px;
  }
  .contact {
    position: absolute;
    left: 89px;
    top: 370px;
    margin: 0;
  }
  .contact-name {
    font-size: 77px;
    line-height: 78px;
    margin: 0;
    font-weight: 400;
  }
  .contact-role {
    font-size: 47px;
    line-height: 50px;
    color: var(--accent-blue);
    margin: 0 0 2px;
  }
  .contact-lines {
    list-style: none;
    margin: 0;
    padding: 0;
    font-size: 45px;
    line-height: 47px;
  }
</style>
</head>
<body>
  <div class="card">
    <div class="cocktail-photo" role="img" aria-label="Photograph of a martini glass with a green olive splashing into it on a black background"></div>

    <div class="brand">
      <div class="brand-square"></div>
      <p class="brand-name">
        <span class="line-main">Corin Vale</span>
        <span class="line-sub">Hospitality College</span>
      </p>
    </div>

    <div class="contact">
      <h1 class="contact-name">Tobin Marsh</h1>
      <p class="contact-role">Director</p>
      <ul class="contact-lines">
        <li>Phone: 1300 615 737</li>
        <li>Mobile: 0455 817 296</li>
        <li>Email: info@corinvale.example</li>
        <li>website: www.corinvale.example</li>
      </ul>
    </div>
  </div>
</body>
</html>
```